Need somewhat upscale, eye catching honey jar label to make our product stand out on store shelves.

We need front and back labels for a honey jar. Files "Honey Jar Front Label 2" & "Honey Jar Back Label 2" show what I have come up with.

Files "Honey Jar Front Label 2". I did this as an example. It shows the information that needs to be included on the front label. The picture was taken by my daughter. The information and picture can be rearranged, enlarged, reduced, cropped, etc. as you see fit.

Files "Honey Jar Back Label 2". I did this one to play with the wording to get the information to fit. It explains how I keep bees. It can be worded differently as long as all the information is included.

I know nothing about good use of color, borders, backgrounds, font style and size, etc. so please excuse my plain presentations. I admire and respect your creative abilities very much.

Since my method of keeping bees involves a lot of travel time and expense, as mentioned in files "Honey Jar Back Label 2" I will try to price my honey a little higher than the competition so please design accordingly with that in mind.

We think we want to use a traditional jar with stick on labels like Marlow's jar seen in file Marlow's Jar. However, feel free to use a different jar as long as the honey can be easily scooped out with a spoon and does not have to be poured out. I know that eliminates a lot of fancy jars but that's what my customers want. Jar size should be 12 ounces which will hold a little more than 1 pound of honey.

Hanging labels are also acceptable therefore jar shapes that will not accept a stick on label can also be used. An example is a Honeypot Jar.

And of course we like Hexagon Jars which are 6 sided like the cells in honeycomb.

Please stick to glass jars that are readily available. No custom shaped jars for now.

Marlow's jar is clear glass and the metal lid is a light golden color.

It's probably a good idea for the shape of the labels to match the shape of the bottle like I marked in black on Marlow's Jar. Being wider in the middle should allow the back label to be shorter than my example seen in files "Honey Jar Back Label 2". I think front and back labels should be the same size.

The shape of the area marked in black around Marlow's label measures 1-1/4 (1.25) inches across the top, 2-1/4 (2.25) inches across the middle, 2 inches across the bottom and 3-1/2 (3.5) inches tall from top to bottom.

Target Market(s)

People wanting local honey that is not processed in any way.
People that are willing to pay a little more for honey from bees that are kept in a sustainable way (see the story in files 2 & 17) without the use of harsh chemicals.

Industry/Entity Type

Travel

Font styles to use
Serif
Decorative
Script

Requirements
Must have
• See my lengthy project description, file "Honey Jar Front Label 2" and file "Honey Jar Back Label 2". All of the info. therein is very important.
• Somewhat upscale, eye catching appearance that makes the product stand out on store shelves and suggests that the honey inside is quality, unprocessed truly local honey.
Nice to have
• If bullets are used they can look like a skep (type of beehive). I have included an example in a file.
• Swirly dashed line coming off the s in lin-Wren's with a honeybee at the end of it. See files for examples.
• Swirly dashed line coming off the i in wildflower making the shape of a heart with a honeybee at the end of it hovering over the o in wildflower and the o looks like a flower. See files for examples.

```html
<!DOCTYPE html>
<html lang="en">
<head>
<meta charset="UTF-8">
<title>lin-Wren's Local Honey – Wildflower Label</title>
<link href="https://fonts.googleapis.com/css2?family=Cinzel:wght@700&family=Dancing+Script:wght@600&family=Caveat:wght@500&family=Lobster&family=Open+Sans:wght@400;600&display=swap" rel="stylesheet">
<style>
  :root {
    --page: #ffffff;
    --label-dark: #1c0c14;
    --gold: #f2c81c;
    --gold-deep: #c99a12;
    --gold-light: #fbe36a;
    --cream: #f4ecd2;
    --amber: #f5a623;
    --wildflower: #d9621a;
    --tagline: #2a1518;
    --white: #ffffff;
  }
  html, body {
    margin: 0;
    padding: 0;
    width: 927px;
    height: 1200px;
    overflow: hidden;
    background: var(--page);
  }
  .canvas {
    position: relative;
    width: 927px;
    height: 1200px;
  }
  .label {
    position: absolute;
    left: 143px;
    top: 100px;
    width: 640px;
    height: 1000px;
  }
  .label-shape {
    position: absolute;
    inset: 0;
    width: 640px;
    height: 1000px;
  }
  .label-text {
    position: absolute;
    left: 0;
    width: 640px;
    text-align: center;
    margin: 0;
  }
  .brand-name {
    top: 48px;
    font-family: "Dancing Script", cursive;
    font-weight: 600;
    font-size: 66px;
    line-height: 1;
    color: var(--cream);
  }
  .product-local {
    top: 190px;
    font-family: "Cinzel", serif;
    font-weight: 700;
    font-size: 58px;
    line-height: 1;
    color: var(--gold);
  }
  .product-honey {
    top: 252px;
    font-family: "Cinzel", serif;
    font-weight: 700;
    font-size: 88px;
    line-height: 1;
    color: var(--gold);
  }
  .tagline {
    position: absolute;
    left: 28px;
    top: 652px;
    margin: 0;
    font-family: "Caveat", cursive;
    font-weight: 500;
    font-size: 28px;
    color: var(--tagline);
  }
  .variety {
    top: 712px;
    font-family: "Lobster", cursive;
    font-size: 52px;
    line-height: 1;
    color: var(--wildflower);
  }
  .qualities {
    top: 808px;
    font-family: "Open Sans", sans-serif;
    font-weight: 600;
    font-size: 23px;
    line-height: 37px;
    color: var(--amber);
  }
  .net-weight {
    top: 928px;
    font-family: "Open Sans", sans-serif;
    font-weight: 400;
    font-size: 18px;
    color: var(--white);
  }
</style>
</head>
<body>
<main class="canvas">
  <section class="label">
    <svg class="label-shape" viewBox="0 0 640 1000" xmlns="http://www.w3.org/2000/svg" aria-hidden="false">
      <defs>
        <path id="label-outline" d="M96 8 H544 C596 8 632 250 632 400 V640 C632 800 606 992 596 992 H44 C34 992 8 800 8 640 V400 C8 250 44 8 96 8 Z"/>
        <clipPath id="label-clip">
          <use href="#label-outline"/>
        </clipPath>
        <linearGradient id="flower-photo-tones" x1="0" y1="0" x2="0" y2="1">
          <stop offset="0" stop-color="#2c3a26"/>
          <stop offset="0.35" stop-color="#4d5a38"/>
          <stop offset="0.58" stop-color="#c9608e"/>
          <stop offset="0.8" stop-color="#f06fab"/>
          <stop offset="1" stop-color="#f58bbb"/>
        </linearGradient>
        <linearGradient id="gold-band" x1="0" y1="0" x2="0" y2="1">
          <stop offset="0" stop-color="var(--gold-deep)"/>
          <stop offset="0.45" stop-color="var(--gold-light)"/>
          <stop offset="1" stop-color="var(--gold-deep)"/>
        </linearGradient>
      </defs>

      <use href="#label-outline" fill="var(--label-dark)"/>

      <g clip-path="url(#label-clip)">
        <path class="flower-photo" role="img"
              aria-label="Photo of a honeybee gathering pollen from a pink hibiscus flower"
              d="M0 372 Q320 330 640 372 V702 H0 Z"
              fill="url(#flower-photo-tones)"/>
        <rect class="variety-band" x="0" y="702" width="640" height="84" fill="url(#gold-band)"/>
      </g>

      <use href="#label-outline" fill="none" stroke="var(--gold)" stroke-width="12"/>
    </svg>

    <p class="label-text brand-name">lin-Wren's</p>
    <h1 class="label-text product-local">LOCAL</h1>
    <h2 class="label-text product-honey">HONEY</h2>
    <p class="tagline">She Works Hard For The Honey</p>
    <p class="label-text variety">Wildflower</p>
    <p class="label-text qualities">100% Pure, Raw, Unaltered<br>Never Heated<br>Strained Not Micro-Filtered</p>
    <p class="label-text net-weight">Net Weight 16 oz / 454g &nbsp;(24 liquid oz)</p>
  </section>
</main>
</body>
</html>
```